label for selfmade spirits, start-up, quality product

Hey there, my name is Tobias, I am 24 years old, living in the southwest of Germany. In the last two years I did experiment: I produced my own spirits. I used self-produced fruit and distilled it in my families small distillery. Distilling has been a tradition in my family, now I want to start my own production and sales. In our region distilling fruit is a tradition but it is in the hand of well-established families / producers. I am planning to establish a quality product with a modern design to focus more on younger people and to sell my spirits to bars, restaurants and private consumers. I did two varieties: "Rilo plum variety" and "Mirabelle de Nancy". (Mirabelle) I am looking for a label design. The bottles will have 0.7 liters, white glass (due to the clear color of the spirits), in a modern bottle: https://www.glasbergkontor.de/behaelter-und-karaffen/destillate/destillatflaschen/rigel-418 , html taste: clear and noble fruit character in the nose, fine flavor of the respective fruit. During the distillation process I tried to capture the natural aroma of the fruit. Therefore, I did a 2nd distilation which is a special feature, that not everybody does. Rilo Zwetschgen Brand "/" Mirabelle de Nancy Brand "- I am also open for. The design can be: - simple and classy, ​​with a valuable appearance that shows in its font, which is the product itself 3 generations were involved in the production, my grandpa gave me important hints, .. I am so open for all ideas that could catch the target group. the label could be printed on either a white or cream label paper. If you have any questions don`t hesitate to contact me, I am looking forward to your suggestions! Cheers!

Target Market(s)

young adults, urban people, people with an interest in a high quality product, ars / restaurants / private customers

Font styles to use
Decorative
Script

Colors

Designer to choose colors to be used in the design.

Requirements
Must have
• So, there are some things that have been posted on the label, due to legal restrictions: - my address: Tobias Wendelbrunn, Lindenweg 5, 68417 Kaiserbach - alcohol level: "alc. 42% vol." - capacity: "0.70 L"; size at least 4 mm - batch number: "L"; please leave an empty space to fill in by hand this information has not been discussed, but should not be too much in the foreground, nor attract to much attention.

```html
<!DOCTYPE html>
<html lang="de">
<head>
<meta charset="utf-8">
<title>Rilo Zwetschge – Etikett</title>
<link href="https://fonts.googleapis.com/css2?family=Marcellus&display=swap" rel="stylesheet">
<style>
  :root {
    --backdrop: #e6e7e9;
    --label-black: #17130d;
    --panel-black: #1d1a14;
    --gold: #d9ad45;
    --gold-light: #f3dc8a;
    --gold-deep: #a87a22;
    --gold-dark: #6d4d14;
    --ink: #2a1d08;
    --seal-plum: #3a2440;
    --seal-wood: #a8773e;
  }
  * { margin: 0; padding: 0; box-sizing: border-box; }
  html, body { width: 1200px; height: 1013px; overflow: hidden; }
  body {
    background: var(--backdrop);
    font-family: "Marcellus", Georgia, serif;
    position: relative;
  }
  .label {
    position: absolute;
    left: 228px;
    top: 76px;
    width: 743px;
    height: 860px;
  }
  .label-body {
    position: absolute;
    left: 0; top: 103px;
    width: 743px; height: 757px;
    background: var(--label-black);
    border-radius: 14px;
  }
  .seal-tab {
    position: absolute;
    left: 237px; top: 0;
    width: 270px; height: 200px;
    background: var(--label-black);
    border-radius: 135px 135px 0 0;
  }
  .frame-ornament {
    position: absolute;
    left: 22px; top: 125px;
    width: 699px; height: 680px;
    border-radius: 10px;
    border: 28px solid transparent;
    background:
      linear-gradient(var(--label-black), var(--label-black)) padding-box,
      linear-gradient(160deg, var(--gold-deep), var(--gold-light) 35%, var(--gold-deep) 60%, var(--gold-light) 85%, var(--gold-deep)) border-box;
    opacity: 0.85;
  }
  .seal {
    position: absolute;
    left: 268px; top: 37px;
    width: 196px; height: 196px;
    border-radius: 50%;
    background: radial-gradient(circle, var(--gold-light) 0 55%, var(--gold) 70%, var(--gold-deep) 100%);
  }
  .seal-picture {
    position: absolute;
    left: 30px; top: 30px;
    width: 136px; height: 136px;
    border-radius: 50%;
    border: 4px solid var(--gold-dark);
    background: linear-gradient(160deg, var(--seal-wood) 0 45%, var(--seal-plum) 70%, #e29a2e 100%);
  }
  .title-panel {
    position: absolute;
    left: 123px; top: 233px;
    width: 507px; height: 327px;
    background: var(--panel-black);
    border-radius: 22px;
  }
  .brand-name {
    position: absolute;
    left: 0; right: 0; top: 262px;
    text-align: center;
    font-size: 170px;
    font-weight: 400;
    line-height: 1;
    color: var(--gold);
    letter-spacing: 8px;
  }
  .variety {
    position: absolute;
    left: 0; right: 0; top: 452px;
    text-align: center;
    font-size: 80px;
    line-height: 1;
    color: var(--gold);
  }
  .info-panel {
    position: absolute;
    left: 77px; top: 546px;
    width: 613px; height: 237px;
    border-radius: 10px;
    background: linear-gradient(180deg, var(--gold-deep) 0%, var(--gold) 18%, var(--gold-light) 45%, var(--gold) 75%, var(--gold-deep) 100%);
  }
  .producer {
    position: absolute;
    left: 0; right: 0; top: 561px;
    text-align: center;
    font-size: 21px;
    color: var(--ink);
  }
  .volume {
    position: absolute;
    left: 0; right: 0; top: 602px;
    text-align: center;
    font-size: 28px;
    color: var(--ink);
  }
  .batch {
    position: absolute;
    left: 287px; top: 651px;
    width: 176px; height: 56px;
    border-radius: 14px;
    background: linear-gradient(180deg, #fbeaa6, #f1d679);
    font-size: 21px;
    color: var(--ink);
    padding: 8px 0 0 10px;
  }
  .alcohol {
    position: absolute;
    left: 0; right: 0; top: 817px;
    text-align: center;
    font-size: 27px;
    color: var(--gold-light);
  }
</style>
</head>
<body>
  <main class="label">
    <div class="label-body"></div>
    <div class="seal-tab"></div>
    <div class="frame-ornament" role="img" aria-label="Ornate gold filigree frame around the label"></div>
    <div class="seal">
      <div class="seal-picture" role="img" aria-label="Oak barrel with ripe plums and a cut fruit"></div>
    </div>
    <div class="title-panel"></div>
    <div class="info-panel" role="img" aria-label="Embossed gold panel with scrollwork"></div>
    <h1 class="brand-name">Rilo</h1>
    <p class="variety">Zwetschge</p>
    <p class="producer">Tobias Wendelbrunn, Lindenweg 5, 68417 Kaiserbach</p>
    <p class="volume">0,70 L</p>
    <p class="batch">Batch number:</p>
    <p class="alcohol">Alc. 42% vol.</p>
  </main>
</body>
</html>
```